Clean & Inspiring Web Design Project

Larkspur Prototype Studio, LLC (also known as LP-Studio) is a company which provides 3D printing services and products. The emphasis is on making these products and services available to the mass-market - customers and users who may or may not have prior experience with 3D printing and/or rapid prototyping technologies. We are a start-up company, looking to build a clean and creativity inspiring brand - our site must encourage visitor to engage and make something. Our aim is to help take mere ideas and turn them into tangible items. We want to show a fusion of ideas (e.g. pencil sketches on graph paper) with design tools (e.g. CAD and drafting software) and rapid prototyping (e.g. TinkNod 3D printers, Stereolithography Machines, etc.). We would like the website to appear professional but at the same time easy to navigate and a good balance between text and pictures. The final design should inspire customers to nurture their ideas into real products and communicate our services to our customers. Our site should have the feel of a vibrant social community with the added benefit of tangible physical creations.

Target Market(s)

People with great ideas that need to be designed into a real product

Industry/Entity Type

Printing

Requirements
Must have
• - Website design should include 2 layouts - one for a "landing page" and one for a "content page"
- Website design must incorporate attached company logo (or derivative of this logo)
- Website design should incorporate the menu options shown in the attached PDF UI concept (UI does not necessarily need to look like the provided concept, just include all the clickable elements)
- Website design must portray an innovative and cooperative design environment with a look-and-feel that appeals to both amateur and professional designers.
- Please include pictures, illustrations and photographs (as needed) related to 3D printing, CAD design, conventional drafting, engineering and manufacturing industries.
- Design should support scaling to multiple screen sizes, from tablet computers (e.g. Slabix) to very large screen PCs.
- Design should include Username & Password fields for login or a button to pull up a login popup.
Nice to have
• - Website design could include "Invent", "Make", "Produce" and "Buy" options that slowly cycle through - with appropriate photos / graphics. These "menu options" would also be mouse-over enabled to switch into the appropriate context as the cursor enters that region (e.g. mouse over the "Invent" text would bring up page 2, etc.). (See attached Original UI Thoughts)
Should not have
• Requirements - Should Not Have:
- Website design should not portray a service that is very expensive or complicated - we are a reasonably priced service meant to be friendly with amateur inventors
- Website design should not be overly complicated - please keep it reasonably simple
- Website design should not be overly trendy
- Website design should not use more than 2 font styles, gaudy fonts, etc.
- Website design should not be "campy" or "tacky" - playful is ok, but please keep it elegant
- Website design should not be overly masculine or feminine - we will have both women and men as customers

```html
<!DOCTYPE html>
<html lang="en">
<head>
<meta charset="utf-8">
<title>LP-Studio · Bringing Your Ideas to Market</title>
<link rel="stylesheet" href="https://fonts.googleapis.com/css2?family=Source+Sans+3:wght@400;600;700&family=Noto+Serif:ital,wght@1,700&display=swap">
<style>
:root{
  --blue:#1a629a;
  --blue-dark:#0f4d7c;
  --blue-mid:#2d7bb3;
  --blue-light:#d9e8f3;
  --ink:#1f5f93;
  --grey-bg:#e7e8e9;
  --white:#ffffff;
  --field:#e9eaeb;
}
*{box-sizing:border-box;margin:0;padding:0}
html,body{width:1045px;height:1200px;overflow:hidden}
body{
  position:relative;
  font-family:"Source Sans 3",Arial,sans-serif;
  background:linear-gradient(#ffffff 0,#ffffff 60px,#dcdddf 300px,#f4f4f5 348px,#ffffff 360px);
  color:var(--ink);
}
.abs{position:absolute}

/* header */
.brand{left:179px;top:14px;display:flex;align-items:center;gap:8px;white-space:nowrap}
.brand-mark{width:24px;height:24px;border:3px solid var(--blue);background:var(--white);flex:none}
.brand-name{font-size:23px;font-weight:600;color:var(--blue);line-height:1}
.main-nav{top:24px;left:327px;font-size:13px;font-weight:600;color:var(--blue-dark)}
.main-nav a{position:absolute;white-space:nowrap;color:inherit;text-decoration:none}
.login{left:700px;top:10px}
.login-field{width:148px;height:18px;background:var(--field);margin-bottom:2px;font-size:10px;font-weight:600;color:var(--blue-dark);padding:2px 5px}
.login-go{left:857px;top:14px;width:28px;height:28px;border-radius:50%;background:var(--blue-dark)}

/* hero */
.hero{left:159px;top:61px;width:726px;height:253px;border-radius:4px;overflow:hidden;
  background:radial-gradient(ellipse at 75% 60%,#5d9ccb 0,#2a74ad 45%,#16588c 100%)}
.hero-backdrop{position:absolute;left:0;top:0;width:100%;height:100%}
.hero-sub{left:446px;top:121px;font-size:20px;color:var(--white);font-weight:400}
.hero-title{left:446px;top:155px;font-family:"Noto Serif",Georgia,serif;font-style:italic;font-weight:700;font-size:33px;line-height:42px;color:var(--white)}
.hero-dots{left:470px;top:283px;display:flex;gap:8px}
.hero-dots span{width:17px;height:17px;border-radius:50%;border:2px solid var(--white);background:rgba(255,255,255,.15)}
.hero-dots span.on{background:var(--white);box-shadow:inset 0 0 0 3px #6fa3cc}

/* news strip */
.news-text{left:171px;top:333px;font-size:16px;color:var(--white);white-space:nowrap}
.news-text em{font-family:"Noto Serif",Georgia,serif;font-weight:700;font-size:17px}

/* content column */
.column{left:150px;top:369px;width:745px;height:666px;background:var(--white)}

/* service rows */
.service-icon{width:100px;height:100px;border-radius:50%;
  background:linear-gradient(#ffffff,#e3e7ea);
  box-shadow:0 3px 0 #bcd3e6,0 4px 8px rgba(0,0,0,.18)}
.service-icon svg{position:absolute;left:25px;top:25px;width:50px;height:50px}
.service-title{font-size:29px;font-weight:400;color:var(--blue);line-height:1;letter-spacing:.3px}
.service-copy{font-size:15px;font-weight:600;color:var(--blue);line-height:18px;margin-top:3px;white-space:nowrap}
.photo{width:133px;height:94px;border:4px solid var(--white);box-shadow:0 1px 5px rgba(0,0,0,.35)}

/* footer */
.footer{left:0;top:1035px;width:1045px;height:165px;background:var(--grey-bg)}
.footer h3{font-size:14px;font-weight:600;color:var(--blue);letter-spacing:.2px;white-space:nowrap}
.about-copy{font-size:11px;line-height:13px;color:var(--blue);width:128px;margin-top:6px}
.contact-row{display:flex;align-items:center;gap:14px;font-size:14px;color:var(--blue-dark);height:22px;white-space:nowrap}
.contact-row svg{width:20px;height:20px;flex:none}
.divider{left:631px;top:1063px;width:2px;height:113px;background:var(--blue-dark)}
.social{display:flex;gap:16px;margin-top:14px}
.social span{width:24px;height:24px;border-radius:50%;background:var(--blue)}
</style>
</head>
<body>

<!-- header -->
<div class="abs brand"><span class="brand-mark"></span><span class="brand-name">LP-Studio</span></div>
<nav class="abs main-nav">
  <a style="left:0">Invent</a>
  <a style="left:65px">Make</a>
  <a style="left:122px">Produce</a>
  <a style="left:196px">Buy</a>
</nav>
<form class="abs login">
  <div class="login-field">Login</div>
  <div class="login-field">Password</div>
</form>
<div class="abs login-go">
  <svg width="28" height="28" viewBox="0 0 28 28"><path d="M11 8 L17 14 L11 20" fill="none" stroke="#fff" stroke-width="3" stroke-linecap="round" stroke-linejoin="round"/></svg>
</div>

<!-- hero -->
<section class="abs hero">
  <div class="hero-backdrop" role="img" aria-label="Blurred close-up of a 3D printed lattice object in blue tones"></div>
</section>
<svg class="abs" style="left:153px;top:122px" width="236" height="126" viewBox="0 0 236 126">
  <path d="M0,4 H236 L200,122 H0 L22,63 Z" fill="#f2f2f2"/>
  <path d="M200,122 L236,4 V12 L206,122 Z" fill="#c9c9c9"/>
</svg>
<div class="abs" style="left:160px;top:140px;width:175px;height:92px;background:radial-gradient(ellipse at 50% 50%,#e6e2d8,#c9c4b6 70%,#eeeeee)" role="img" aria-label="3D printed threaded cylinder part"></div>
<div class="abs hero-sub">Larkspur Prototype Studio, LLC</div>
<h1 class="abs hero-title">Bringing Your Ideas<br>to Market</h1>
<div class="abs hero-dots"><span class="on"></span><span></span><span></span></div>

<!-- news strip -->
<svg class="abs" style="left:127px;top:322px" width="783" height="52" viewBox="0 0 783 52">
  <path d="M0,4 H22 V50 L8,44 Z" fill="#0b3f66"/>
  <path d="M783,4 H760 V50 L775,44 Z" fill="#0b3f66"/>
  <path d="M14,2 H769 L762,24 L769,47 H14 L21,24 Z" fill="#1a5d8c"/>
  <path d="M734,16 L742,24 L734,32" fill="none" stroke="#fff" stroke-width="3.5" stroke-linecap="round" stroke-linejoin="round"/>
</svg>
<p class="abs news-text">You can write a few words about current news / events / <em>special offers!</em> / ETC. of LP-Studio here...</p>

<!-- content column -->
<div class="abs column"></div>

<svg width="0" height="0" style="position:absolute">
  <defs>
    <linearGradient id="panel-fill" x1="0" x2="1" y1="0" y2="0">
      <stop offset="0" stop-color="#dce9f3"/>
      <stop offset="0.22" stop-color="#5d9bc9"/>
      <stop offset="0.45" stop-color="#1f679e"/>
      <stop offset="1" stop-color="#114f80"/>
    </linearGradient>
  </defs>
</svg>

<!-- INVENT -->
<svg class="abs" style="left:523px;top:384px" width="380" height="126" viewBox="0 0 380 126">
  <path d="M364,0 L380,4 V14 H364 Z" fill="#0b3f66"/>
  <path d="M0,6 H372 Q380,6 380,14 V116 Q380,124 372,124 H0 L56,65 Z" fill="url(#panel-fill)"/>
</svg>
<div class="abs photo" style="left:585px;top:402px;background:radial-gradient(#c8b48c,#6b5e48 60%,#2b2b2b)" role="img" aria-label="Ornate 3D printed sculpture"></div>
<div class="abs photo" style="left:748px;top:402px;background:radial-gradient(#e8eef2,#8aa0ad 60%,#3c4a55)" role="img" aria-label="3D printed lattice sphere"></div>
<div class="abs service-icon" style="left:159px;top:394px">
  <svg viewBox="0 0 50 50"><path d="M25 5a14 14 0 0 0-8 25.5V36h16v-5.5A14 14 0 0 0 25 5z" fill="none" stroke="#1a629a" stroke-width="4" stroke-linejoin="round"/><rect x="18" y="39" width="14" height="4" rx="2" fill="#1a629a"/><rect x="20" y="45" width="10" height="3" rx="1.5" fill="#1a629a"/></svg>
</div>
<div class="abs" style="left:273px;top:408px">
  <h2 class="service-title">INVENT</h2>
  <p class="service-copy">Have an idea?<br>We can make it REAL</p>
</div>

<!-- MAKE -->
<svg class="abs" style="left:523px;top:541px" width="380" height="132" viewBox="0 0 380 132">
  <path d="M364,0 L380,4 V14 H364 Z" fill="#0b3f66"/>
  <path d="M0,6 H372 Q380,6 380,14 V122 Q380,130 372,130 H0 L56,68 Z" fill="url(#panel-fill)"/>
</svg>
<div class="abs photo" style="left:585px;top:563px;background:linear-gradient(135deg,#e8632b,#2f2f2f 45%,#3a78c4 75%,#f2c230)" role="img" aria-label="Assorted colourful 3D printed parts"></div>
<div class="abs photo" style="left:748px;top:563px;background:radial-gradient(#eeeae0,#c7c2b3 65%,#f4f4f4)" role="img" aria-label="3D printed threaded cylinder part"></div>
<div class="abs service-icon" style="left:159px;top:558px">
  <svg viewBox="0 0 50 50"><path d="M21 4h8l1.5 6 4.5 2 5.5-3 5.5 5.5-3 5.5 2 4.5 6 1.5v8l-6 1.5-2 4.5 3 5.5-5.5 5.5-5.5-3-4.5 2L29 46h-8l-1.5-6-4.5-2-5.5 3-5.5-5.5 3-5.5-2-4.5L4 29v-8l6-1.5 2-4.5-3-5.5L14.5 4l5.5 3 4.5-2z" fill="#1a629a"/><circle cx="25" cy="25" r="7" fill="#fff"/></svg>
</div>
<div class="abs" style="left:271px;top:570px">
  <h2 class="service-title">MAKE</h2>
  <p class="service-copy">Need an idea? We have them!<br>Have a design? We can sell it!</p>
</div>

<!-- PRODUCE -->
<svg class="abs" style="left:139px;top:711px;transform:scaleX(-1)" width="385" height="136" viewBox="0 0 385 136">
  <path d="M369,0 L385,4 V14 H369 Z" fill="#0b3f66"/>
  <path d="M0,6 H377 Q385,6 385,14 V126 Q385,134 377,134 H0 L56,70 Z" fill="url(#panel-fill)"/>
</svg>
<div class="abs photo" style="left:162px;top:737px;background:linear-gradient(135deg,#dcc4a4,#b07f52 50%,#e2cba9)" role="img" aria-label="3D printed honeycomb pattern panel"></div>
<div class="abs photo" style="left:324px;top:737px;background:radial-gradient(#ffffff,#c9cccf 55%,#5b5f63)" role="img" aria-label="3D printed interlocking ring sculpture"></div>
<div class="abs service-icon" style="left:521px;top:730px">
  <svg viewBox="0 0 50 50">
    <path d="M12 42 L34 20" stroke="#1a629a" stroke-width="6" stroke-linecap="round"/>
    <path d="M24 8 L36 20 L42 14 L30 2 Z" fill="#1a629a"/>
    <path d="M38 42 L18 22" stroke="#1a629a" stroke-width="5" stroke-linecap="round"/>
    <path d="M9 6a8 8 0 0 0 10 11l-4-4 1-4 4-1 4 4A8 8 0 0 0 13 4z" fill="#1a629a"/>
  </svg>
</div>
<div class="abs" style="left:634px;top:748px">
  <h2 class="service-title">PRODUCE</h2>
  <p class="service-copy">Have a Machine? We can use it!<br>Have a design? We can deliver it!</p>
</div>

<!-- BUY -->
<svg class="abs" style="left:139px;top:873px;transform:scaleX(-1)" width="385" height="136" viewBox="0 0 385 136">
  <path d="M369,0 L385,4 V14 H369 Z" fill="#0b3f66"/>
  <path d="M0,6 H377 Q385,6 385,14 V126 Q385,134 377,134 H0 L56,70 Z" fill="url(#panel-fill)"/>
</svg>
<div class="abs photo" style="left:162px;top:899px;background:linear-gradient(160deg,#d9d4cc,#6f5f4f 55%,#2c2622)" role="img" aria-label="3D printed high-heel shoe"></div>
<div class="abs photo" style="left:324px;top:899px;background:radial-gradient(#f0dcae,#b08a4c 45%,#1b1712 80%)" role="img" aria-label="3D printed lamp shade glowing"></div>
<div class="abs service-icon" style="left:521px;top:899px">
  <svg viewBox="0 0 50 50"><path d="M8 12 H42 L39 42 Q38 45 35 45 H15 Q12 45 11 42 Z" fill="#1a629a"/><rect x="6" y="8" width="38" height="6" rx="2" fill="#1a629a"/><path d="M17 20 Q25 30 33 20" fill="none" stroke="#fff" stroke-width="3.5" stroke-linecap="round"/></svg>
</div>
<div class="abs" style="left:644px;top:910px">
  <h2 class="service-title">BUY</h2>
  <p class="service-copy">Find one you like?<br>We can make and deliver it!</p>
</div>

<!-- footer -->
<footer class="abs footer"></footer>
<div class="abs" style="left:186px;top:1100px;width:28px;height:28px;border:3px solid var(--blue);background:#fff"></div>
<div class="abs" style="left:240px;top:1068px">
  <h3>ABOUT US</h3>
  <p class="about-copy">Something short about LP-Studio. Something short about LP-Studio. Something short about LP-Studio.</p>
</div>
<div class="abs" style="left:399px;top:1068px">
  <h3>CUSTOMER SERVICE</h3>
  <div style="margin-top:12px">
    <div class="contact-row"><svg viewBox="0 0 20 20"><path d="M4 2 L8 2 L9 7 L6.5 8.5 Q8 12 11.5 13.5 L13 11 L18 12 V16 Q18 18 16 18 Q3 17 2 4 Q2 2 4 2Z" fill="#1f5f93"/></svg>+ 11 555 010 200</div>
    <div class="contact-row" style="margin-top:10px"><svg viewBox="0 0 20 20"><circle cx="10" cy="10" r="8" fill="#1f5f93"/></svg>chatname@name</div>
    <div class="contact-row" style="margin-top:8px"><svg viewBox="0 0 20 20"><rect x="1.5" y="4" width="17" height="12" fill="none" stroke="#1f5f93" stroke-width="1.6"/><path d="M1.5 4 L10 11 L18.5 4 M1.5 16 L8 10 M18.5 16 L12 10" fill="none" stroke="#1f5f93" stroke-width="1.6"/></svg>lpstudio@mail.com</div>
  </div>
</div>
<div class="abs divider"></div>
<div class="abs" style="left:657px;top:1067px">
  <h3>GET SOCIAL!</h3>
  <div class="social"><span></span><span></span><span></span></div>
</div>

</body>
</html>
```